Business Card Design Project

Design a business card for a new entity that is in the OTC (over-the-counter-derivative brokering business-Financial Services.
The card should be clean a professional looking. We encourage designers to think pro-actively, fresh and innovative, but also keep in mind that only 2 things are important. a)that the card look professional b)that it is somehow memorable.

We have a new logo which we will upload and will want the Trident symbol in the logo to be raised OR not have the symbol raised and plan on having the word " BROKERAGE SERVICES" raised that stands out and will look sharp.

Along with uploading the new logo which MUST be incorperated, I am also going to upload 3 different business cards of other businesses to use only as guild-lines since I think they are clean and professional looking BUT I encourage all to be pro-active and creative on their own.

Industry/Entity Type

Business

Requirements
Must have
• 1. MUST HAVE THE NEW LOGO WHICH WILL BE UPLOADED
2. MUST HAVE A VERSION SIMILAR TO THE 3 DIFFERENT BUSINESS CARDS I WILL UPLOAD, BUT EACH DESIGNER MUST ONLY THESE THIS FORMAT AS A BACK-UP AND BE CREATIVE ON THEIR OWN FIRST. ALSO WHEN LOOKING AT THE CARDS WHICH I UPLOAD TO USE AS A GUILD-LINE KEEP IN MIND THAT THESE ARE KESTRAVEL 300 COMPANIES SO DO NOT MIMIC ONLY USE FOR IDEAS.
Nice to have
• these are the 3 different other biz cards to look at for some reference

```html
<!DOCTYPE html>
<html lang="en">
<head>
<meta charset="utf-8">
<title>Halvard Brokerage Services – Business Card</title>
<link rel="stylesheet" href="https://fonts.googleapis.com/css2?family=Marcellus&family=Open+Sans:wght@400;600&display=swap">
<style>
  :root {
    --page: #ececea;
    --card: #ffffff;
    --band: #474948;
    --gold: #c4962f;
    --ink: #3f4141;
    --ink-soft: #5a5c5c;
    --shadow: rgba(0, 0, 0, 0.18);
  }
  * { box-sizing: border-box; margin: 0; padding: 0; }
  html, body {
    width: 1200px;
    height: 900px;
    overflow: hidden;
    background: var(--page);
    font-family: "Open Sans", Arial, sans-serif;
    color: var(--ink);
  }
  .stage {
    position: relative;
    width: 1200px;
    height: 900px;
    display: flex;
    align-items: center;
    justify-content: center;
    gap: 40px;
  }
  .card {
    position: relative;
    width: 540px;
    height: 310px;
    background: var(--card);
    box-shadow: 0 10px 24px var(--shadow);
    overflow: hidden;
  }
  .card__band {
    position: absolute;
    top: 0;
    right: 0;
    width: 58px;
    height: 100%;
    background: var(--band);
  }
  .card__marker {
    position: absolute;
    top: 26px;
    right: 40px;
    width: 40px;
    height: 44px;
  }

  /* Wordmark */
  .wordmark {
    font-family: "Marcellus", Georgia, serif;
    color: var(--ink);
    display: flex;
    align-items: center;
    gap: 14px;
  }
  .wordmark__dot {
    width: 16px;
    height: 16px;
    background: var(--gold);
    flex: none;
  }
  .wordmark__text {
    display: flex;
    flex-direction: column;
    line-height: 1.05;
    letter-spacing: 0.12em;
  }
  .wordmark__name { font-size: 44px; }
  .wordmark__tag { font-size: 15px; letter-spacing: 0.22em; margin-top: 4px; }

  /* Back */
  .card--back .wordmark {
    position: absolute;
    left: 82px;
    top: 112px;
  }
  .back__contact {
    position: absolute;
    right: 0;
    top: 0;
    width: 58px;
    height: 100%;
    display: flex;
    align-items: flex-end;
    justify-content: center;
    padding-bottom: 26px;
  }
  .back__contact-list {
    writing-mode: vertical-rl;
    transform: rotate(180deg);
    display: flex;
    gap: 18px;
    color: #f2f2f2;
    font-size: 11px;
    letter-spacing: 0.02em;
  }
  .back__contact-list span { display: flex; align-items: center; gap: 6px; }
  .back__contact-list svg { width: 10px; height: 10px; transform: rotate(90deg); }

  /* Front */
  .card--front .wordmark {
    position: absolute;
    left: 30px;
    bottom: 32px;
  }
  .card--front .wordmark__name { font-size: 36px; }
  .card--front .wordmark__tag { font-size: 13px; }
  .person {
    position: absolute;
    left: 190px;
    top: 40px;
  }
  .person__name { font-size: 22px; font-weight: 400; color: var(--ink); line-height: 1.1; }
  .person__title { font-size: 14px; color: var(--ink-soft); }
  .contact {
    position: absolute;
    left: 290px;
    top: 116px;
    font-size: 13px;
    color: var(--ink);
    line-height: 1.45;
  }
  .contact__group { margin-bottom: 10px; }
  .contact__row { display: flex; align-items: center; gap: 7px; }
  .contact__icon {
    width: 15px;
    height: 15px;
    border: 1px solid var(--ink-soft);
    background: var(--gold);
    display: flex;
    align-items: center;
    justify-content: center;
    flex: none;
  }
  .contact__icon svg { width: 9px; height: 9px; }
</style>
</head>
<body>
<main class="stage">

  <!-- Card back: wordmark with contact strip -->
  <section class="card card--back" aria-label="Business card back">
    <div class="wordmark">
      <span class="wordmark__dot"></span>
      <div class="wordmark__text">
        <span class="wordmark__name">HALVARD</span>
        <span class="wordmark__tag">BROKERAGE SERVICES</span>
      </div>
    </div>
    <div class="card__band"></div>
    <svg class="card__marker" viewBox="0 0 40 44" aria-hidden="true">
      <polygon points="40,0 40,44 2,22" fill="#ffffff"/>
      <polygon points="37,6 37,38 9,22" fill="var(--gold)"/>
    </svg>
    <div class="back__contact">
      <div class="back__contact-list">
        <span>
          <svg viewBox="0 0 10 10" aria-hidden="true"><rect x="0.5" y="2" width="9" height="6" fill="none" stroke="#f2f2f2"/><polyline points="0.5,2 5,6 9.5,2" fill="none" stroke="#f2f2f2"/></svg>
          name@name.com
        </span>
        <span>
          <svg viewBox="0 0 10 10" aria-hidden="true"><circle cx="5" cy="5" r="4.3" fill="none" stroke="#f2f2f2"/><line x1="0.7" y1="5" x2="9.3" y2="5" stroke="#f2f2f2"/><ellipse cx="5" cy="5" rx="2" ry="4.3" fill="none" stroke="#f2f2f2"/></svg>
          www.webname.com
        </span>
      </div>
    </div>
  </section>

  <!-- Card front: person and contact details -->
  <section class="card card--front" aria-label="Business card front">
    <div class="card__band"></div>
    <svg class="card__marker" viewBox="0 0 40 44" aria-hidden="true">
      <polygon points="40,0 40,44 2,22" fill="#ffffff"/>
      <polygon points="37,6 37,38 9,22" fill="var(--gold)"/>
    </svg>

    <div class="person">
      <h1 class="person__name">Your Name</h1>
      <p class="person__title">job title</p>
    </div>

    <div class="contact">
      <div class="contact__group">
        <div class="contact__row">Your Address goes here</div>
        <div class="contact__row">
          <span class="contact__icon"><svg viewBox="0 0 10 10" aria-hidden="true"><path d="M2 1 L4 1 L4.6 3.2 L3.4 4 Q4.5 6 6 6.6 L6.8 5.4 L9 6 L9 8 Q5 9 1 4 Z" fill="#fff"/></svg></span>
          000-000-0000
        </div>
        <div class="contact__row">
          <span class="contact__icon"><svg viewBox="0 0 10 10" aria-hidden="true"><rect x="2.5" y="0.5" width="5" height="9" rx="1" fill="none" stroke="#fff"/><circle cx="5" cy="7.8" r="0.7" fill="#fff"/></svg></span>
          000-000-0000
        </div>
      </div>
      <div class="contact__group">
        <div class="contact__row">
          <span class="contact__icon"><svg viewBox="0 0 10 10" aria-hidden="true"><rect x="0.5" y="2" width="9" height="6" fill="none" stroke="#fff"/><polyline points="0.5,2 5,6 9.5,2" fill="none" stroke="#fff"/></svg></span>
          name@domainname.com
        </div>
        <div class="contact__row">
          <span class="contact__icon"><svg viewBox="0 0 10 10" aria-hidden="true"><circle cx="5" cy="5" r="4.3" fill="none" stroke="#fff"/><line x1="0.7" y1="5" x2="9.3" y2="5" stroke="#fff"/><ellipse cx="5" cy="5" rx="2" ry="4.3" fill="none" stroke="#fff"/></svg></span>
          www.websitename.com
        </div>
      </div>
    </div>

    <div class="wordmark">
      <span class="wordmark__dot"></span>
      <div class="wordmark__text">
        <span class="wordmark__name">HALVARD</span>
        <span class="wordmark__tag">BROKERAGE SERVICES</span>
      </div>
    </div>
  </section>

</main>
</body>
</html>
```